Fun, challenging, and inspirational guide for life change - written by a coach, therapist and founde

I need (1) cover design for a book titled:
"THE WANDERER'S TOOLKIT FOR MIND-SHIFTING IDEAS" - the surprisingly practical magic of believing and taking action

A 2ND COVER will be need for a companion ebook, titled:
"THE HEARTH LEDGER FOR PURPOSE AND CONTENTMENT - 3 steps to help unlock and unleash the unlimited you by loving your limitations

These books will be used to promote a larger suite of products and services devoted to empowering and inspiring a community of OVERCOMERS.

For reference check out www.brightquillpath.com

I've included some photos for visual reference points.

DESIGNS CONCEPTS:
CLEAN - A BLEND OF PAST AND PRESENT - MODERN AND THE SACRED) (...The Marlowe's Atlas meets

Target Market(s)

young and aspiring professionals and seasoned pros looking for life-changes due to feeling unfulfilled in their profession and relationships

Industry/Entity Type

Life Coaching

Font styles to use
Serif
Sans Serif

Requirements
Must have
• CREATIVITY - ORIGINALITY - WICKEDLY CLEAN DESIGN- AND IMPACTFUL TRANSLATION OF BRAND CONCEPT - COLOR AND PUNCH
Nice to have
• I included some photos as reference point - **PLEASE SEE THE PHOTOS FOR THE STAR-GAZERS DESIGNS** - I really like the feeling they provoke - I want to give the viewer a sense of the journey that can be taken when they dive into these books.
• Basically, riff off the design profiles and colors included in the STAR-GAZER covers.
• MUSTS INCLUDE -
• -ORIGINALITY
• - IMPACT
• - COLOR
• - ORIGINAL DESIGNS+
• +
Should not have
• STAY AWAY FROM...
• 1 OVERUSED AND TRENDY ICONS
• - ESOTERIC IMAGES
• - FLOWERY SCRIPTS
• - I AM REALLY LOOKING FOR A UPDATE OF THE TYPICAL SELF-HELP BOOK COVERS WHICH RELY TOO MUCH ON FLOWERY AND SACRED IMAGERY
• THANK YOU - feel free to unleash your creativity!

```html
<!DOCTYPE html>
<html lang="en">
<head>
<meta charset="utf-8">
<title>Book Cover Pair</title>
<link rel="stylesheet" href="https://fonts.googleapis.com/css2?family=Barlow:wght@500;600&family=Barlow+Condensed:wght@500;600&family=Tinos:ital@1&display=swap">
<style>
  :root {
    --orange: #f0673d;
    --green: #3f9b40;
    --white: #ffffff;
    --cream: #f4efc2;
    --lavender: #dde0ef;
    --arch-frame: #1d1a16;
    --ink: #1a1410;
  }
  html, body {
    margin: 0;
    padding: 0;
    width: 1200px;
    height: 900px;
    overflow: hidden;
  }
  .spread {
    position: relative;
    width: 1200px;
    height: 900px;
    display: flex;
  }
  .cover {
    position: relative;
    width: 600px;
    height: 900px;
    overflow: hidden;
  }
  .cover--hearth { background: var(--orange); }
  .cover--wanderer { background: var(--green); }

  .title {
    position: absolute;
    left: 0;
    right: 0;
    margin: 0;
    text-align: center;
    text-transform: uppercase;
  }
  .cover--hearth .title {
    top: 30px;
    font-family: "Barlow", sans-serif;
    font-weight: 600;
    font-size: 49px;
    line-height: 46px;
    letter-spacing: 0.5px;
    color: var(--white);
  }
  .cover--wanderer .title {
    top: 28px;
    font-family: "Barlow Condensed", sans-serif;
    font-weight: 600;
    font-size: 74px;
    line-height: 77px;
    letter-spacing: 0.5px;
    color: var(--cream);
  }

  .arch {
    position: absolute;
  }
  .cover--hearth .arch { left: 106px; top: 229px; width: 387px; height: 602px; }
  .cover--wanderer .arch { left: 143px; top: 330px; width: 320px; height: 501px; }
  .arch svg { display: block; width: 100%; height: 100%; }

  .subtitle {
    position: absolute;
    left: 0;
    right: 0;
    margin: 0;
    text-align: center;
    font-family: "Tinos", serif;
    font-style: italic;
    color: var(--ink);
  }
  .cover--hearth .subtitle { top: 104px; font-size: 19px; line-height: 24px; }
  .cover--wanderer .subtitle { top: 87px; font-size: 19px; line-height: 24px; }

  .author {
    position: absolute;
    left: 0;
    right: 0;
    top: 840px;
    margin: 0;
    text-align: center;
    font-family: "Barlow", sans-serif;
    font-weight: 500;
    font-size: 38px;
    letter-spacing: 5px;
    line-height: 44px;
  }
  .cover--hearth .author { color: var(--lavender); }
  .cover--wanderer .author { color: var(--cream); }
</style>
</head>
<body>
<main class="spread">

  <section class="cover cover--hearth">
    <h1 class="title">The Hearth<br>Ledger for<br>Purpose and<br>Contentment</h1>
    <div class="arch">
      <svg viewBox="0 0 387 602" role="img" aria-label="Photo of a lone traveller walking through a stone archway toward a sunlit city street">
        <defs>
          <radialGradient id="glow-hearth" cx="0.5" cy="0.55" r="0.65">
            <stop offset="0" stop-color="#fff3c4"/>
            <stop offset="0.35" stop-color="#e9b64e"/>
            <stop offset="0.7" stop-color="#8a6428"/>
            <stop offset="1" stop-color="#2f2518"/>
          </radialGradient>
        </defs>
        <path d="M0,602 V193.5 A193.5,193.5 0 0 1 387,193.5 V602 Z" fill="var(--arch-frame)"/>
        <path d="M24,602 V193.5 A169.5,169.5 0 0 1 363,193.5 V602 Z" fill="url(#glow-hearth)"/>
      </svg>
      <p class="subtitle">3 steps to help you<br>unlock and unleash<br>the unlimited you<br>by understanding<br>your limitations</p>
    </div>
    <p class="author">AUTHOR NAME</p>
  </section>

  <section class="cover cover--wanderer">
    <h1 class="title">The Wanderer's<br>Toolkit for<br>Mind-Shifting<br>Ideas</h1>
    <div class="arch">
      <svg viewBox="0 0 320 501" role="img" aria-label="Photo of a lone traveller walking through a stone archway toward a sunlit city street">
        <defs>
          <radialGradient id="glow-wanderer" cx="0.5" cy="0.55" r="0.65">
            <stop offset="0" stop-color="#fff3c4"/>
            <stop offset="0.35" stop-color="#e9b64e"/>
            <stop offset="0.7" stop-color="#8a6428"/>
            <stop offset="1" stop-color="#2f2518"/>
          </radialGradient>
        </defs>
        <path d="M0,501 V160 A160,160 0 0 1 320,160 V501 Z" fill="var(--arch-frame)"/>
        <path d="M20,501 V160 A140,140 0 0 1 300,160 V501 Z" fill="url(#glow-wanderer)"/>
      </svg>
      <p class="subtitle">the surprisingly<br>practical magic<br>of believing<br>and taking action</p>
    </div>
    <p class="author">AUTHOR NAME</p>
  </section>

</main>
</body>
</html>
```